Real Estate For Sale Signage

I'm an independent agent in Lismore NSW Australia with high standards and looking for a catching 'For Sale'sign board.
I like classy, elegant, stylish and simple best.
My colours are red, white and black.
I don't have a logo or other font designs I need to stick to. I like the concept of a house or real estate design.
Before I created this project I played around on publisher and created the PDF attached. I'm not sold on it, but I don't mind the way the name has been layed out. Originally I had a white background with black & red font.
Fancy fonts for my name would be nice, but must not be busy.
Updates

Just wanted to advise that I have updated my brief and used the tools available to help get my ideas through.

Thank you for your work and time.

Kind regards
Marella

Industry/Entity Type

Real Estate

Requirements
Must have
• For Sale
Marella Quint Real Estate (must stand out)
0400 517 382 (must stand out)
17 Tallowood Street North Lismore
www.marellaquintrealestate.com.au

```html
<!DOCTYPE html>
<html lang="en">
<head>
<meta charset="utf-8">
<title>For Sale – Marella Quint Real Estate</title>
<link rel="stylesheet" href="https://fonts.googleapis.com/css2?family=Cinzel:wght@700&family=Libre+Baskerville:ital,wght@0,700;1,700&display=swap">
<style>
  :root {
    --page-bg: #e9e6e1;
    --sign-black: #0d0d0d;
    --sign-red: #d0121a;
    --sign-red-light: #f02a2a;
    --sign-red-deep: #9e0a10;
    --ornament-tone: #b80d15;
    --ink-white: #ffffff;
  }
  * { margin: 0; padding: 0; box-sizing: border-box; }
  html, body {
    width: 1200px;
    height: 900px;
    overflow: hidden;
    background: var(--page-bg);
  }
  .canvas {
    width: 1200px;
    height: 900px;
    display: flex;
    align-items: center;
    justify-content: center;
  }
  .sign {
    width: 1000px;
    height: 750px;
    background: var(--sign-black);
    padding: 22px;
  }
  .sign-face {
    position: relative;
    width: 100%;
    height: 100%;
    background: radial-gradient(ellipse at 50% 45%, var(--sign-red-light) 0%, var(--sign-red) 45%, var(--sign-red-deep) 100%);
  }
  .sign-frame {
    position: absolute;
    inset: 22px;
    border: 3px solid var(--ink-white);
  }
  .corner-ornament {
    position: absolute;
    width: 44px;
    height: 44px;
    background: var(--ornament-tone);
    border-radius: 50%;
  }
  .corner-ornament.top-left { top: 6px; left: 6px; }
  .corner-ornament.top-right { top: 6px; right: 6px; }
  .corner-ornament.bottom-left { bottom: 6px; left: 6px; }
  .corner-ornament.bottom-right { bottom: 6px; right: 6px; }
  .sign-content {
    position: absolute;
    inset: 0;
    display: flex;
    flex-direction: column;
    align-items: center;
    color: var(--ink-white);
    text-align: center;
    padding-top: 46px;
  }
  .headline {
    font-family: "Cinzel", serif;
    font-weight: 700;
    font-size: 112px;
    line-height: 1;
    letter-spacing: 2px;
  }
  .connector,
  .phone-label {
    font-family: "Libre Baskerville", serif;
    font-style: italic;
    font-weight: 700;
    font-size: 36px;
    line-height: 1;
  }
  .connector { margin-top: 16px; }
  .agency-name {
    font-family: "Libre Baskerville", serif;
    font-weight: 700;
    color: var(--ink-white);
    line-height: 1.1;
    margin-top: 18px;
  }
  .agency-name-main {
    display: block;
    font-size: 80px;
  }
  .agency-name-sub {
    display: block;
    font-size: 40px;
    letter-spacing: 2px;
    margin-top: 6px;
  }
  .phone-label { margin-top: 28px; }
  .phone-number {
    font-family: "Libre Baskerville", serif;
    font-weight: 700;
    font-size: 84px;
    line-height: 1;
    margin-top: 16px;
    letter-spacing: 2px;
  }
  .contact-line {
    font-family: "Libre Baskerville", serif;
    font-style: italic;
    font-weight: 700;
    font-size: 22px;
    line-height: 1.3;
  }
  .contact-line.web { margin-top: 30px; }
</style>
</head>
<body>
  <main class="canvas">
    <section class="sign" aria-label="For Sale sign">
      <div class="sign-face">
        <div class="sign-frame">
          <div class="corner-ornament top-left" role="img" aria-label="Decorative corner flourish"></div>
          <div class="corner-ornament top-right" role="img" aria-label="Decorative corner flourish"></div>
          <div class="corner-ornament bottom-left" role="img" aria-label="Decorative corner flourish"></div>
          <div class="corner-ornament bottom-right" role="img" aria-label="Decorative corner flourish"></div>
        </div>
        <div class="sign-content">
          <h1 class="headline">FOR SALE</h1>
          <p class="connector">with</p>
          <p class="agency-name">
            <span class="agency-name-main">Marella Quint</span>
            <span class="agency-name-sub">Real Estate</span>
          </p>
          <p class="phone-label">phone</p>
          <p class="phone-number">0400 517 382</p>
          <p class="contact-line web">www.MarellaQuintRealEstate.com.au</p>
          <p class="contact-line address">17 Tallowood Street, North Lismore</p>
        </div>
      </div>
    </section>
  </main>
</body>
</html>
```